Purely Windswept needs an eye catching marketing flyer

Our new Luminous Airflow(r) business needs an eye catching marketing flyer. We think A5 sizing?
website link (where you can understand more about breathwork is www.purelywindswept.co.uk)
Design whatever you would like to design some things that could be of use to mention are below. Will leave it in your capable hands.
Logo files for Purely Windswept attached, use whichever one is best for your design, should be the main logo and colour scheme for the flyer, the second logo is that of Luminous Airflow(r) the breath school who's body of work we will be delivering. This can be anywhere on the flyer
Flyer is needed to get people interested in breathwork, the potential benefits for breathing better
We offer 1:1 sessions, workshops, corporate training
The flyer will have an offer code 'OpenGlow' which will give 15% off the bookers first 1:1 session
Flyer should include the following contact details: Maybe a "find out how breathwork can help you today. . . "
Tessa Orchard (South): 07700 318 527
Lorraine Pitt (Midlands): 07700 452 183
facebook: we.are.purelywindswept
instagram: _purelywindswept_

```html
<!DOCTYPE html>
<html lang="en">
<head>
<meta charset="utf-8">
<title>Purely Windswept – Breathwork Flyer</title>
<link rel="stylesheet" href="https://fonts.googleapis.com/css2?family=Montserrat:wght@300;400;500;600;700;800&family=Oswald:wght@500;600&display=swap">
<style>
  :root {
    --page-bg: #e6e6e4;
    --paper: #f4f4f5;
    --royal: #1f3fb5;
    --navy: #1b2a6e;
    --violet: #7b55c8;
    --teal: #3cc4cf;
    --badge-top: #62667f;
    --badge-bottom: #2a2d47;
    --forest-light: #6f9a78;
    --forest-dark: #274a33;
    --sky: #b9d3df;
    --grove-light: #3f6a3a;
    --grove-dark: #0f2414;
    --white: #ffffff;
  }
  * { margin: 0; padding: 0; box-sizing: border-box; }
  html, body {
    width: 1200px; height: 900px; overflow: hidden;
    background: var(--page-bg);
    font-family: "Montserrat", sans-serif;
  }
  .flyer-stage {
    position: absolute; left: 296px; top: 20px;
    width: 607px; height: 860px;
  }
  .flyer {
    position: absolute; left: 0; top: 0;
    width: 720px; height: 1020px;
    transform: scale(0.843); transform-origin: 0 0;
    background: var(--paper);
    overflow: hidden;
    box-shadow: 0 6px 24px rgba(0,0,0,0.18);
  }
  .flyer-shapes { position: absolute; inset: 0; width: 720px; height: 1020px; }

  .brand-seal {
    position: absolute; left: 458px; top: 280px;
    width: 244px; height: 244px; border-radius: 50%;
    background: #efeff0;
    box-shadow: 0 4px 14px rgba(0,0,0,0.12);
    display: flex; align-items: center; justify-content: center;
    text-align: center;
  }
  .brand-name {
    font-family: "Montserrat", sans-serif;
    font-weight: 500; font-size: 27px; line-height: 1.2;
    color: var(--navy);
  }

  .offer-badge {
    position: absolute; left: 36px; top: 486px;
    width: 228px; height: 228px; border-radius: 50%;
    padding: 4px;
    background: linear-gradient(160deg, var(--violet), var(--royal) 50%, var(--teal));
    box-shadow: 0 14px 18px -8px rgba(0,0,0,0.35);
  }
  .offer-badge-inner {
    width: 100%; height: 100%; border-radius: 50%;
    background: radial-gradient(circle at 50% 25%, var(--badge-top), var(--badge-bottom) 80%);
    color: var(--white); text-align: center;
    display: flex; flex-direction: column; justify-content: center; align-items: center;
  }
  .offer-label { font-weight: 300; font-size: 25px; line-height: 1.1; }
  .offer-code { font-weight: 700; font-size: 24px; letter-spacing: 0.5px; margin-top: 4px; }
  .offer-amount { font-weight: 700; font-size: 37px; line-height: 1.05; letter-spacing: 1px; }
  .offer-terms { font-weight: 400; font-size: 16px; line-height: 1.6; letter-spacing: 0.3px; }

  .services { position: absolute; left: 282px; top: 540px; width: 392px; text-align: right; }
  .services-title { font-weight: 800; font-size: 68px; line-height: 1; color: var(--royal); letter-spacing: -0.5px; }
  .services-main { font-weight: 700; font-size: 25px; color: var(--violet); margin-top: 6px; }
  .services-sub { font-weight: 700; font-size: 31px; color: var(--teal); line-height: 1.1; }

  .contact { position: absolute; left: 46px; top: 748px; width: 360px; }
  .contact-lead { font-weight: 800; font-size: 19px; color: var(--navy); line-height: 1; }
  .contact-lead-large { font-weight: 800; font-size: 27px; color: var(--navy); line-height: 1.1; }
  .contact-list { margin-top: 10px; }
  .contact-name { font-weight: 500; font-size: 17.5px; color: var(--royal); line-height: 23px; }
  .contact-phone { font-weight: 700; font-size: 18px; color: var(--royal); line-height: 23px; }
  .social { margin-top: 10px; }
  .social-line { display: flex; align-items: center; gap: 7px; font-size: 13px; color: #444a66; line-height: 18px; }
  .social-dot { width: 11px; height: 11px; border-radius: 50%; background: var(--navy); }
  .address {
    margin-top: 18px;
    font-family: "Oswald", sans-serif; font-weight: 500;
    font-size: 9.5px; color: var(--navy); letter-spacing: 0.2px;
  }
  .website {
    font-family: "Oswald", sans-serif; font-weight: 600;
    font-size: 23px; color: var(--royal); line-height: 1.05; letter-spacing: 0.3px;
  }
</style>
</head>
<body>
<div class="flyer-stage">
  <article class="flyer">
    <svg class="flyer-shapes" viewBox="0 0 720 1020" aria-hidden="false">
      <defs>
        <linearGradient id="band-gradient" x1="0" y1="0" x2="1" y2="0">
          <stop offset="0" stop-color="#2a3db2"/>
          <stop offset="0.7" stop-color="#2f52c4"/>
          <stop offset="1" stop-color="#3cc4cf"/>
        </linearGradient>
        <linearGradient id="band-gradient-low" x1="0" y1="0" x2="1" y2="0">
          <stop offset="0" stop-color="#3a3fb8"/>
          <stop offset="0.6" stop-color="#4f7fd2"/>
          <stop offset="1" stop-color="#3cc4cf"/>
        </linearGradient>
        <radialGradient id="forest-gradient" cx="0.5" cy="0.45" r="0.65">
          <stop offset="0" stop-color="var(--sky)"/>
          <stop offset="0.35" stop-color="var(--forest-light)"/>
          <stop offset="1" stop-color="var(--forest-dark)"/>
        </radialGradient>
        <radialGradient id="grove-gradient" cx="0.55" cy="0.45" r="0.7">
          <stop offset="0" stop-color="var(--grove-light)"/>
          <stop offset="1" stop-color="var(--grove-dark)"/>
        </radialGradient>
      </defs>

      <path d="M0,0 H720 V196 Q660,390 470,470 Q240,540 0,330 Z"
            fill="url(#forest-gradient)" role="img"
            aria-label="Aerial photo of a forest with a lake shaped like a pair of lungs"/>
      <path d="M0,330 Q240,540 470,470" fill="none" stroke="url(#band-gradient)" stroke-width="14"/>

      <path d="M375,1020 V860 Q395,718 560,700 L720,690 V1020 Z"
            fill="url(#grove-gradient)" role="img"
            aria-label="Photo of cupped hands holding a young tree in soil"/>
      <path d="M418,745 Q470,700 560,697 L720,688" fill="none" stroke="url(#band-gradient-low)" stroke-width="11"/>
    </svg>

    <div class="brand-seal">
      <span class="brand-name">Purely<br>Windswept</span>
    </div>

    <div class="offer-badge">
      <div class="offer-badge-inner">
        <span class="offer-label">offer code</span>
        <span class="offer-code">OPENGLOW</span>
        <span class="offer-amount">15% OFF</span>
        <span class="offer-terms">THE BOOKERS FIRST<br>1:1 SESSION</span>
      </div>
    </div>

    <section class="services">
      <h1 class="services-title">WE OFFER</h1>
      <p class="services-main">1:1 SESSIONS | WORKSHOPS</p>
      <p class="services-sub">CORPORATE TRAINING</p>
    </section>

    <section class="contact">
      <p class="contact-lead">FIND OUT HOW BREATHWORK</p>
      <p class="contact-lead-large">CAN HELP YOU TODAY…</p>
      <div class="contact-list">
        <p class="contact-name">TESSA ORCHARD (SOUTH):</p>
        <p class="contact-phone">07700 318 527</p>
        <p class="contact-name">LORRAINE PITT (MIDLANDS):</p>
        <p class="contact-phone">07700 452 183</p>
      </div>
      <div class="social">
        <p class="social-line"><span class="social-dot"></span>/we.are.purelywindswept</p>
        <p class="social-line"><span class="social-dot"></span>@purelywindswept</p>
      </div>
      <p class="address">12 MEADOW LANE, FERNBRIDGE, WEST MIDLANDS, FB1 2AB</p>
      <p class="website">WWW.PURELYWINDSWEPT.CO.UK</p>
    </section>
  </article>
</div>
</body>
</html>
```